Elegant Black Candle Label Design!

I need a 2.375" tall by 3.0" wide candle label design. I'm looking for simple and elegant. Black label with silver leaf border and lettering. Label needs to have the following information on it: Fern Hollow Candle Co. as the company name, scent name in the middle and in smaller font, it needs to say Made in USA, All Natural, 8oz. Attached photos are for inspiration.

Target Market(s)

People looking for high end, all natural candle fragrances

Industry/Entity Type

Candle-Spa

Colors

Designer to choose only greyscale colors for use in the design.

Requirements
Must have
• Company Name, Scent (ability to change scent names), All Natural, Made in USA, 8oz
Nice to have
• Black background, silver leaf border and silver leaf font. Elegant fonts maybe slightly cursive

```html
<!DOCTYPE html>
<html lang="en">
<head>
<meta charset="UTF-8">
<title>Fern Hollow Candle Co. – Lavender Label</title>
<link href="https://fonts.googleapis.com/css2?family=Josefin+Sans:wght@300&family=Poiret+One&display=swap" rel="stylesheet">
<style>
  :root {
    --black: #000000;
    --silver: #d2d3d4;
    --silver-light: #f4f4f4;
    --silver-mid: #bdbdbd;
    --ink: #1a1a1a;
  }
  html, body {
    margin: 0;
    padding: 0;
    width: 1200px;
    height: 1200px;
    overflow: hidden;
    background: var(--black);
  }
  .canvas {
    position: relative;
    width: 1200px;
    height: 1200px;
    background: var(--black);
  }
  .label {
    position: absolute;
    left: 263px;
    top: 300px;
    width: 674px;
    height: 598px;
    box-sizing: border-box;
    border: 10px solid var(--silver);
    border-radius: 54px;
    background: var(--black);
  }
  .brand-name {
    position: absolute;
    left: 0;
    right: 0;
    top: 400px;
    margin: 0;
    text-align: center;
    font-family: "Josefin Sans", sans-serif;
    font-weight: 300;
    font-size: 44px;
    letter-spacing: 3px;
    color: var(--silver);
    line-height: 1;
  }
  .scent-plate {
    position: absolute;
    left: 430px;
    top: 563px;
    width: 340px;
    height: 74px;
    box-sizing: border-box;
    border: 3px solid var(--silver-light);
    border-radius: 18px;
    padding: 4px;
    background: var(--black);
  }
  .scent-plate__face {
    width: 100%;
    height: 100%;
    border-radius: 12px;
    background: linear-gradient(100deg, var(--silver-mid) 0%, var(--silver-light) 35%, #ffffff 55%, #d9d9d9 80%, var(--silver-mid) 100%);
    display: flex;
    align-items: center;
    justify-content: center;
  }
  .scent-name {
    font-family: "Poiret One", sans-serif;
    font-size: 24px;
    letter-spacing: 17px;
    margin-right: -17px;
    color: var(--ink);
  }
  .details {
    position: absolute;
    left: 351px;
    width: 498px;
    font-family: "Josefin Sans", sans-serif;
    font-weight: 300;
    font-size: 22px;
    color: var(--silver-light);
    line-height: 1;
  }
  .details--origin {
    top: 780px;
  }
  .details__rule {
    position: absolute;
    left: 351px;
    top: 809px;
    width: 498px;
    height: 2px;
    background: var(--silver);
  }
  .details--bottom {
    top: 824px;
    display: flex;
    justify-content: space-between;
  }
</style>
</head>
<body>
  <main class="canvas">
    <div class="label"></div>

    <h1 class="brand-name">Fern Hollow Candle Co.</h1>

    <div class="scent-plate">
      <div class="scent-plate__face">
        <span class="scent-name">LAVENDER</span>
      </div>
    </div>

    <div class="details details--origin">Made in USA</div>
    <div class="details__rule"></div>
    <div class="details details--bottom">
      <span class="details__claim">All Natural</span>
      <span class="details__weight">8oz</span>
    </div>
  </main>
</body>
</html>
```